Lip Balm Label Design

Design a label for a Lavender-Mint lip balm. We make high-quality natural essential oil products. Please use the old label as an example of what exists. The label should include purple. The final design should be eye-catching and distinct. The file should be in an AI file.

Here is the information that should be included on the label:
1) ingredients:Theobroma Cacao (Cocoa) Seed Butter, Theobroma grandiflorum Ultra Refined Butter, beesewax, Calendula Officinalis Flower Oil, Prunus Amygdalus Dulcis (Sweet Almond) Oil, cetyl alcohol and Tocopherol. Lavandula Angustifolia (Lavender) Oil and Mentha Piperita (Peppermint) Oil.

2) www.kelvorascent.com

3) Brand name and logo: K. Velora Aromatherapy (logo is attached- you can use with form)

```html
<!DOCTYPE html>
<html lang="en">
<head>
<meta charset="UTF-8">
<title>K. Velora Aromatherapy – Peppermint Lip Balm Label</title>
<link href="https://fonts.googleapis.com/css2?family=Playfair+Display:wght@400;500&family=Montserrat:wght@400;500;600&display=swap" rel="stylesheet">
<style>
  :root {
    --page-bg: #f4f4f5;
    --plum-deep: #2a0042;
    --plum-dark: #3d0060;
    --violet: #8a3ff0;
    --magenta: #c412b8;
    --magenta-deep: #8e0a82;
    --band: #37004f;
    --white: #ffffff;
    --shadow: rgba(40, 0, 60, 0.22);
  }
  * { box-sizing: border-box; margin: 0; padding: 0; }
  html, body {
    width: 1200px; height: 640px; overflow: hidden;
    background: var(--page-bg);
  }
  .canvas {
    position: relative; width: 1200px; height: 640px;
    display: flex; justify-content: center; align-items: center; gap: 32px;
  }
  .label {
    position: relative; width: 290px; height: 572px; overflow: hidden;
    color: var(--white);
    background:
      radial-gradient(ellipse 90% 45% at 80% 100%, var(--magenta) 0%, rgba(196,18,184,0) 70%),
      radial-gradient(ellipse 70% 40% at 0% 62%, var(--violet) 0%, rgba(138,63,240,0) 75%),
      linear-gradient(160deg, var(--plum-dark) 0%, var(--plum-deep) 35%, #5a0a8a 60%, var(--magenta-deep) 100%);
    box-shadow: 0 14px 26px var(--shadow);
  }
  .label__waves { position: absolute; inset: 0; width: 100%; height: 100%; }
  .brand {
    position: absolute; top: 44px; left: 0; right: 0;
    display: flex; flex-direction: column; align-items: center;
    font-family: "Playfair Display", serif; font-weight: 400;
  }
  .brand__dot {
    width: 36px; height: 36px; border-radius: 50%;
    background: var(--white); margin-bottom: 14px;
  }
  .brand__name { font-size: 30px; line-height: 1; letter-spacing: 0.5px; }
  .brand__sub { font-size: 9px; letter-spacing: 1.6px; text-transform: uppercase; margin-top: 4px; }
  .product-title {
    position: absolute; font-family: "Playfair Display", serif; font-weight: 500;
    line-height: 1; color: var(--white);
  }
  .product-title--lip { left: 96px; top: 196px; font-size: 150px; letter-spacing: -4px; }
  .product-title--balm { left: 28px; top: 322px; font-size: 70px; letter-spacing: -2px; }
  .flavour-band {
    position: absolute; left: 0; right: 0; top: 408px; height: 39px;
    background: var(--band);
    display: flex; align-items: center; justify-content: center;
    font-family: "Montserrat", sans-serif; font-weight: 600; font-size: 16px;
    letter-spacing: 7px; padding-left: 7px;
  }
  .net-weight {
    position: absolute; left: 0; right: 0; top: 532px; text-align: center;
    font-family: "Montserrat", sans-serif; font-weight: 500; font-size: 10px; letter-spacing: 0.6px;
  }
  .ingredients {
    position: absolute; left: 0; right: 0; top: 206px; text-align: center;
  }
  .ingredients__title {
    font-family: "Playfair Display", serif; font-weight: 400; font-size: 28px; margin-bottom: 14px;
  }
  .ingredients__list {
    font-family: "Montserrat", sans-serif; font-weight: 400; font-size: 10.2px; line-height: 16px;
    padding: 0 14px;
  }
  .website {
    position: absolute; left: 0; right: 0; top: 410px;
    display: flex; align-items: center; justify-content: center; gap: 10px;
    font-family: "Playfair Display", serif; font-weight: 400; font-size: 20px;
  }
  .website__icon { width: 15px; height: 15px; }
</style>
</head>
<body>
<main class="canvas">

  <section class="label label--front" aria-label="Front label">
    <svg class="label__waves" viewBox="0 0 290 572" preserveAspectRatio="none" aria-hidden="true">
      <path d="M0 160 C60 160 90 120 110 40 C120 10 140 0 160 0 L0 0 Z" fill="rgba(255,255,255,0.06)"/>
      <path d="M290 250 C230 300 200 380 230 470 C250 530 290 560 290 572 Z" fill="rgba(255,255,255,0.07)"/>
      <path d="M120 572 C140 520 150 480 210 460 C250 450 270 430 290 400 L290 572 Z" fill="rgba(255,120,230,0.12)"/>
    </svg>
    <div class="brand">
      <span class="brand__dot"></span>
      <span class="brand__name">K. Velora</span>
      <span class="brand__sub">Aromatherapy</span>
    </div>
    <span class="product-title product-title--lip">lip</span>
    <span class="product-title product-title--balm">balm</span>
    <div class="flavour-band">PEPPERMINT</div>
    <div class="net-weight">0.15OZ</div>
  </section>

  <section class="label label--back" aria-label="Back label">
    <svg class="label__waves" viewBox="0 0 290 572" preserveAspectRatio="none" aria-hidden="true">
      <path d="M0 160 C60 160 90 120 110 40 C120 10 140 0 160 0 L0 0 Z" fill="rgba(255,255,255,0.06)"/>
      <path d="M290 250 C230 300 200 380 230 470 C250 530 290 560 290 572 Z" fill="rgba(255,255,255,0.07)"/>
      <path d="M120 572 C140 520 150 480 210 460 C250 450 270 430 290 400 L290 572 Z" fill="rgba(255,120,230,0.12)"/>
    </svg>
    <div class="ingredients">
      <h2 class="ingredients__title">Ingredients:</h2>
      <p class="ingredients__list">
        Calendula Officinalis Flower Oil, Prunus<br>
        Amygdalus Dulcis (Sweet Almond) Oil,<br>
        Theobroma Cacao Seed Butter,<br>
        beeswax ,cetyl alcohol and Tocopherol,<br>
        Theobroma grandiflorum Ultra Refined Butter,<br>
        Lavandula Angustifolia (Lavender) Oil,<br>
        Mentha Piperita (Peppermint) Oil.
      </p>
    </div>
    <div class="website">
      <svg class="website__icon" viewBox="0 0 16 16" aria-hidden="true">
        <path d="M1 1 L14 5 L9 7 L14 13 L12 15 L7 9 L5 14 Z" fill="#ffffff"/>
      </svg>
      <span>www.kelvorascent.com</span>
    </div>
    <div class="net-weight">0.15OZ</div>
  </section>

</main>
</body>
</html>
```